Cosmetics range packaging

Needing cosmetics logo design with our logo attached and showing you some examples of products we need logo and packaging (cosmetic box) designs.
Products e.g. palette is black so the printing would be a red metallic foil on the lid of the palette as a preference / guide. With the logo it would need to get a white letter M and a red metallic foil star. This is needed for the palette lid and also for the cardboard box packaging.

Some examples of the palette packaging and shape are attached below (competitor brands) just to show you what the shape is.

Target Market(s)

Women 15-60 years of age

Industry/Entity Type

Cosmetics

Requirements
Must have
• Our logo on it and packaging background is black.
Nice to have
• The logo preferably white letter M and red foil metallic star.
Should not have
• Open to ideas

```html
<!DOCTYPE html>
<html lang="en">
<head>
<meta charset="utf-8">
<title>Mireva – Palette Box Dieline</title>
<link rel="stylesheet" href="https://fonts.googleapis.com/css2?family=Montserrat:wght@800&display=swap">
<style>
  :root {
    --paper: #ffffff;
    --cutline: #b9b9b9;
    --box-black: #000000;
    --foil-dark: #5e0f0c;
    --foil-mid: #9a0907;
    --foil-bright: #e30000;
    --foil-line: #d10000;
    --brand-white: #ffffff;
  }
  html, body {
    margin: 0;
    padding: 0;
    width: 1200px;
    height: 1200px;
    overflow: hidden;
    background: var(--paper);
  }
  .dieline {
    display: block;
    width: 1200px;
    height: 1200px;
  }
  .flap { fill: var(--paper); stroke: var(--cutline); stroke-width: 1; }
  .panel { fill: var(--box-black); }
  .foil-rule { fill: var(--foil-line); }
  .brand-plate { fill: var(--box-black); }
  .brand-name {
    font-family: "Montserrat", sans-serif;
    font-weight: 800;
    font-size: 30px;
    letter-spacing: 2px;
    fill: var(--brand-white);
  }
</style>
</head>
<body>
<svg class="dieline" viewBox="0 0 1300 1300" xmlns="http://www.w3.org/2000/svg">
  <defs>
    <linearGradient id="foil-band" x1="162" y1="0" x2="1159" y2="0" gradientUnits="userSpaceOnUse">
      <stop offset="0" stop-color="var(--foil-dark)"/>
      <stop offset="0.22" stop-color="var(--foil-bright)"/>
      <stop offset="0.52" stop-color="var(--foil-dark)"/>
      <stop offset="0.77" stop-color="var(--foil-bright)"/>
      <stop offset="1" stop-color="var(--foil-dark)"/>
    </linearGradient>
  </defs>

  <!-- glue flap -->
  <path class="flap" d="M162 415 L139 423 L139 814 L162 821 Z"/>
  <!-- lid tuck flap -->
  <path class="flap" d="M162 415 L162 398 Q162 386 174 386 L585 386 Q597 386 597 398 L597 415 Z"/>
  <!-- dust flaps -->
  <path class="flap" d="M601 479 L603 449 Q603 445 607 445 L652 445 Q655 445 655 449 L657 479 Z"/>
  <path class="flap" d="M1101 479 L1103 449 Q1103 445 1107 445 L1152 445 Q1155 445 1155 449 L1157 479 Z"/>
  <path class="flap" d="M601 821 L603 851 Q603 854 607 854 L652 854 Q655 854 655 851 L657 821 Z"/>
  <path class="flap" d="M1101 821 L1103 851 Q1103 854 1107 854 L1152 854 Q1155 854 1155 851 L1157 821 Z"/>
  <!-- base tuck flap -->
  <path class="flap" d="M661 884 L661 899 Q661 913 675 913 L1082 913 Q1096 913 1096 899 L1096 884 Z"/>

  <!-- printed panels -->
  <rect class="panel" x="162" y="415" width="436" height="406"/>
  <rect class="panel" x="597" y="479" width="562" height="342"/>
  <rect class="panel" x="661" y="820" width="435" height="64"/>

  <!-- foil band -->
  <rect class="foil-rule" x="162" y="613" width="997" height="3"/>
  <rect x="162" y="620" width="997" height="56" fill="url(#foil-band)"/>
  <rect class="foil-rule" x="162" y="679" width="997" height="3"/>

  <!-- brand mark -->
  <rect class="brand-plate" x="800" y="622" width="156" height="52" rx="4"/>
  <text class="brand-name" x="878" y="659" text-anchor="middle">MIREVA</text>
</svg>
</body>
</html>
```